Dental office needs flyer Design

We need a flier design for our Dental office based in Rockville MD. We provide premium dental care services including General and Ortho.

Flier Audience - Upper Middle Class, Individual professionals, Family, urban living,

Flier Focus - Promote "Grin Circle" program offered by the office
Key Highlights of the program - $69 for individual, $59 per person for family of two, $49 per person for a family 3, $39 per person for a family of 4. Design thoughts - Circle from big size to small with visual representation of individual and family size. The subscription is per month and annual membership, Also with the membership member will receive 15 - 25% of procedures. 3 - 4 cleanings a year, One XRay per year, One Emergency Exam per year, easy monthly payments, No Deductible, No yearly maximums, No Exclusions.

Flier Design considerations
Door Hanger, Eye Catchy shape,

Dental Office Highlights - No more than 9 patients a day so no double booking, no waiting; Before and after hours appointments, weekend appointments are available for emergencies, Direct access to Dentist,

Services Provided
1. Preventative Care
2. Orthodontics - Braces, Clearomet,
3. Cosmetic - Veneers, Teeth Whitening, Bonding
4. Bridges, Implants, Crown, Filling,
5. Dentures
6. Root Canal, Extractions, Gum Treatments

Location - 2836 Thornbury Ln Rockville MD 20853
PH: 301 555 0148
Website : www.DentistKalvo.com

Target Market(s)

Upper Middle Class, Individual professionals, Family, urban living,

Industry/Entity Type

Dental

Font styles to use
Decorative
Script

Requirements
Must have
• Promote "Grin Circle" program offered by the office
• Key Highlights of the program - $69 for individual, $59 per person for family of two, $49 per person for a family 3, $39 per person for a family of 4. Design thoughts - Circle from big size to small with visual representation of individual and family size. The subscription is per month and annual membership, Also with the membership member will receive 15 - 25% of procedures. 3 - 4 cleanings a year, One XRay per year, One Emergency Exam per year, easy monthly payments, No Deductible, No yearly maximums, No Exclusions.
• Location - 2836 Thornbury Ln Rockville MD 20853
• PH: 301 555 0148
• Website : www.DentistKalvo.com
Nice to have
• Eye Catchy Shape for Flier

```html
<!DOCTYPE html>
<html lang="en">
<head>
<meta charset="utf-8">
<title>Grin Circle Flyer</title>
<link href="https://fonts.googleapis.com/css2?family=Roboto+Condensed:wght@300;400;700&family=Lato:wght@400;700&display=swap" rel="stylesheet">
<style>
:root{
  --green:#2e7d32;
  --charcoal:#4d4d4d;
  --ink:#222;
  --text:#333;
  --white:#fff;
  --page:#ffffff;
  --photo-warm-1:#efe7dc;
  --photo-warm-2:#d9c9b4;
  --photo-teal:#9fcdd9;
}
*{box-sizing:border-box;margin:0;padding:0}
html,body{width:1200px;height:1200px;overflow:hidden;background:var(--page)}
.flyer{position:absolute;left:220px;top:78px;width:760px;height:1064px;background:var(--white);overflow:hidden;font-family:'Lato',sans-serif;color:var(--text)}
.flyer svg.shapes{position:absolute;inset:0}
.photo{position:absolute}
.brand{position:absolute;left:36px;top:34px;width:170px;text-align:center}
.brand-mark{width:96px;height:96px;border-radius:50%;background:var(--green);margin:0 auto 14px}
.brand-tagline{font-family:'Lato',sans-serif;font-weight:700;font-size:13px;line-height:1.4;color:var(--ink);text-transform:uppercase}
.headline{position:absolute;left:26px;top:386px;width:390px;font-family:'Roboto Condensed',sans-serif;white-space:nowrap}
.headline .lead{font-weight:700;font-size:40px;color:var(--charcoal);line-height:1.1}
.headline .premium{font-weight:700;font-size:26px;color:var(--green);line-height:1.4;letter-spacing:0}
.headline .scope{font-weight:400;font-size:34px;color:var(--charcoal);line-height:1.25}
.program-name{position:absolute;left:62px;top:514px;font-family:'Roboto Condensed',sans-serif;font-weight:700;font-size:58px;color:var(--green);white-space:nowrap}
.tab{position:absolute;height:26px;border-radius:0 13px 13px 0;background:var(--charcoal);color:var(--white);font-family:'Roboto Condensed',sans-serif;font-size:19px;line-height:26px;padding-left:26px;white-space:nowrap}
.tab-program{top:598px;left:0;width:264px}
.tab-office{top:769px;left:0;width:222px}
.tab-services{top:710px;left:419px;width:196px;background:var(--white);color:var(--green);font-weight:700;padding-left:34px}
.bullets{position:absolute;list-style:none;font-size:11px;line-height:13.6px;color:var(--text);white-space:nowrap}
.bullets li{position:relative;padding-left:9px}
.bullets li::before{content:"";position:absolute;left:0;top:5px;width:4px;height:4px;border-radius:50%;background:var(--green)}
.program-list{left:26px;top:641px;width:362px}
.program-list li{margin-bottom:6px}
.office-list{left:26px;top:808px;width:360px}
.office-list li{margin-bottom:5px}
.service-list{left:452px;top:750px;width:300px;color:var(--white);font-weight:700}
.service-list li{margin-bottom:5px;padding-left:0}
.service-list li::before{left:-11px;border-radius:0;width:5px;height:5px;background:var(--green)}
.call{position:absolute;left:26px;top:906px;font-family:'Roboto Condensed',sans-serif;font-weight:700;font-size:35px;color:var(--green);white-space:nowrap}
.call .number{color:var(--charcoal)}
.contact{position:absolute;left:28px;color:var(--white);font-size:13px;display:flex;align-items:center;gap:6px;white-space:nowrap}
.contact svg{width:11px;height:13px}
.contact-address{top:1010px}
.contact-web{top:1032px}
.price{position:absolute;border-radius:50%;background:var(--white);border:4px solid var(--green);display:flex;flex-direction:column;align-items:center;justify-content:center;text-align:center;color:var(--ink);font-family:'Lato',sans-serif;white-space:nowrap}
.price .amount{font-family:'Roboto Condensed',sans-serif;font-weight:700;color:var(--green)}
.price-individual{left:380px;top:510px;width:188px;height:188px}
.price-individual .row{display:flex;align-items:baseline;gap:6px;font-size:30px}
.price-individual .row .amount{font-size:58px;line-height:1}
.price-individual .label{font-size:30px;line-height:1.05}
.price-two{left:559px;top:491px;width:160px;height:160px}
.price-two .row{display:flex;align-items:baseline;font-size:19px}
.price-two .row .amount{font-size:38px;line-height:1}
.price-two .label{font-size:19px;line-height:1.25}
.price-three{left:607px;top:364px;width:140px;height:140px}
.price-three .amount{font-size:32px;line-height:1.1}
.price-three .label{font-size:19px;line-height:1.3}
.price-four{left:604px;top:251px;width:120px;height:120px}
.price-four .amount{font-size:28px;line-height:1.05}
.price-four .label{font-size:18px;line-height:1.2}
</style>
</head>
<body>
<main class="flyer">
  <svg class="shapes" viewBox="0 0 760 1064" width="760" height="1064">
    <rect class="services-panel" x="419" y="300" width="341" height="764" fill="var(--charcoal)"/>
    <path class="content-backdrop" d="M0 360 H419 V1064 H0Z" fill="var(--white)"/>
  </svg>

  <svg class="photo photo-family" role="img" aria-label="Photo of a smiling family of four lying on a soft rug at home" viewBox="0 0 760 380" width="760" height="380" style="left:0;top:0">
    <defs>
      <linearGradient id="familyTone" x1="0" y1="0" x2="1" y2="1">
        <stop offset="0" stop-color="var(--photo-warm-1)"/>
        <stop offset=".55" stop-color="var(--photo-teal)"/>
        <stop offset="1" stop-color="var(--photo-warm-2)"/>
      </linearGradient>
    </defs>
    <path d="M0 0 H760 V298 C600 330 500 362 380 366 C250 370 110 330 0 266 Z" fill="url(#familyTone)"/>
  </svg>

  <svg class="shapes" viewBox="0 0 760 1064" width="760" height="1064" style="pointer-events:none">
    <path class="brand-corner" d="M0 0 H230 C190 60 235 150 175 200 C135 232 70 230 0 215 Z" fill="var(--white)" stroke="var(--green)" stroke-width="8"/>
    <path class="wave-grey" d="M0 290 C110 352 250 386 380 382 C500 378 600 346 760 312" fill="none" stroke="var(--charcoal)" stroke-width="6"/>
    <path class="wave-green" d="M0 266 C110 330 250 370 380 366 C500 362 600 330 760 298" fill="none" stroke="var(--green)" stroke-width="10"/>
    <path class="footer-grey" d="M0 950 C140 1000 300 990 430 940" fill="none" stroke="var(--charcoal)" stroke-width="6"/>
    <path class="footer-green" d="M0 968 C160 1016 320 1000 470 944 C580 905 680 890 760 892 V1064 H0Z" fill="var(--green)"/>
  </svg>

  <svg class="photo photo-team" role="img" aria-label="Photo of three smiling dentists in teal scrubs" viewBox="0 0 354 176" width="354" height="176" style="left:406px;top:888px">
    <defs>
      <linearGradient id="teamTone" x1="0" y1="0" x2="0" y2="1">
        <stop offset="0" stop-color="#6b5a4e"/>
        <stop offset=".45" stop-color="#c9a58b"/>
        <stop offset="1" stop-color="#5aaec4"/>
      </linearGradient>
    </defs>
    <path d="M0 176 V70 C40 30 90 8 150 4 C230 0 300 10 354 22 V176Z" fill="url(#teamTone)"/>
  </svg>

  <div class="brand">
    <div class="brand-mark"></div>
    <p class="brand-tagline">Excellence in care,<br>skill and judgement</p>
  </div>

  <div class="headline">
    <p class="lead">We provide</p>
    <p class="premium">PREMIUM DENTAL CARE SERVICES</p>
    <p class="scope">including General and Ortho</p>
  </div>
  <h1 class="program-name">Grin Circle</h1>

  <div class="tab tab-program">Key Highlights of the program</div>
  <ul class="bullets program-list">
    <li>Design thoughts - Circle from big size to small with visual<br>representation of individual and family size.</li>
    <li>The subscription is per month and annual membership, Also with the<br>membership member will receive 15 - 25% of procedures.</li>
    <li>3 - 4 cleanings a year, One XRay per year, One Emergency Exam per year,<br>easy monthly payments, No Deductible, No yearly maximums,<br>No Exclusions.</li>
  </ul>

  <div class="tab tab-office">Dental Office Highlights</div>
  <ul class="bullets office-list">
    <li>No more than 9 patients a day so no double booking,</li>
    <li>no waiting</li>
    <li>Before and after hours appointments</li>
    <li>weekend appointments are available for emergencies</li>
    <li>Direct access to Dentist</li>
  </ul>

  <p class="call">CALL : <span class="number">301 555 0148</span></p>

  <p class="contact contact-address">
    <svg viewBox="0 0 11 14"><path d="M5.5 0A5 5 0 0 0 .5 5c0 3.6 5 9 5 9s5-5.4 5-9a5 5 0 0 0-5-5Zm0 7a2 2 0 1 1 0-4 2 2 0 0 1 0 4Z" fill="var(--white)"/></svg>
    2836 Thornbury Ln Rockville MD 20853
  </p>
  <p class="contact contact-web">
    <svg viewBox="0 0 12 12"><circle cx="6" cy="6" r="5" fill="none" stroke="var(--white)" stroke-width="1.4"/><path d="M1 6H11M6 1C3.5 4 3.5 8 6 11M6 1C8.5 4 8.5 8 6 11" fill="none" stroke="var(--white)" stroke-width="1"/></svg>
    www.DentistKalvo.com
  </p>

  <div class="tab tab-services">Services Provided</div>
  <ul class="bullets service-list">
    <li>Preventative Care</li>
    <li>Orthodontics - Braces, Clearomet,</li>
    <li>Cosmetic - Veneers, Teeth Whitening, Bonding</li>
    <li>Bridges, Implants, Crown, Filling,</li>
    <li>Dentures</li>
    <li>Root Canal, Extractions, Gum Treatment</li>
  </ul>

  <div class="price price-four">
    <span class="amount">$39</span>
    <span class="label">person for<br>a family<br>of 4</span>
  </div>
  <div class="price price-three">
    <span class="amount">$49</span>
    <span class="label">per person for<br>a family</span>
  </div>
  <div class="price price-two">
    <span class="row"><span class="amount">$59</span>per</span>
    <span class="label">person for<br>family of two</span>
  </div>
  <div class="price price-individual">
    <span class="row"><span class="amount">$69</span>for</span>
    <span class="label">individual</span>
  </div>
</main>
</body>
</html>
```